I want to revise my business card design and get a more modern and up to date design.

uMendo Handyman Sevices originated from a family-owned and operated contractor business, performing home renovation, addition, and construction work in the NYC area since 2004. Today, we specialize in reliable and affordable handyman services for residential and commercial clients In 2014, we expanded to northern New Jersey. In 2016, we brought quality home improvement and repair services to new Bucks County, PA, and nearby New Jersey areas.
Target Market(s)
Home owners and business that might be looking for a General contractor, handyman, cleaning services and Home maintenance and property.
Industry/Entity Type
Construction Company
Contact Information for Business Card
I am open to new ideas
Colors
Designer to choose colors to be used in the design.
Look and feel

```html
<!DOCTYPE html>
<html lang="en">
<head>
<meta charset="utf-8">
<title>uMendo Handyman Sevices – Business Card</title>
<link rel="stylesheet" href="https://fonts.googleapis.com/css2?family=Roboto:wght@300;400;500;700;900&display=swap">
<style>
  :root {
    --brand-red: #ec1c24;
    --ink: #111111;
    --paper: #ffffff;
    --muted: #555555;
    --rule: #9a9a9a;
    --canvas: #e9e6e1;
  }
  * { box-sizing: border-box; margin: 0; padding: 0; }
  html, body { width: 1200px; height: 1040px; overflow: hidden; }
  body {
    background: var(--canvas);
    font-family: "Roboto", sans-serif;
    position: relative;
  }
  .card {
    position: absolute;
    left: 180px;
    width: 840px;
    height: 480px;
    box-shadow: 0 8px 24px rgba(0,0,0,.18);
    overflow: hidden;
  }
  .card--front { top: 30px; background: var(--paper); }
  .card--back { top: 530px; background: var(--brand-red); }

  /* Front */
  .brand {
    position: absolute;
    right: 60px;
    top: 52px;
    display: flex;
    align-items: center;
    gap: 14px;
  }
  .brand__dot {
    width: 26px; height: 26px;
    border-radius: 50%;
    background: var(--brand-red);
  }
  .brand__text { display: flex; flex-direction: column; }
  .brand__name {
    font-weight: 900;
    font-size: 64px;
    line-height: 1;
    color: var(--ink);
    letter-spacing: -1px;
  }
  .brand__tagline {
    font-weight: 400;
    font-size: 11px;
    letter-spacing: 4px;
    color: var(--muted);
    margin-top: 6px;
  }
  .contact {
    position: absolute;
    left: 60px;
    top: 300px;
  }
  .contact__name {
    font-weight: 700;
    font-size: 30px;
    color: var(--brand-red);
    letter-spacing: -0.5px;
  }
  .contact__rule {
    position: absolute;
    left: 60px; top: 352px;
    width: 730px; height: 1px;
    background: var(--rule);
  }
  .contact__list {
    position: absolute;
    left: 60px; top: 364px;
    list-style: none;
    font-weight: 300;
    font-size: 19px;
    color: #333;
  }
  .contact__list li { display: flex; align-items: center; gap: 10px; height: 30px; }
  .contact__list svg { width: 16px; height: 16px; flex: none; }
  .card__band { position: absolute; left: 0; bottom: 0; width: 840px; height: 70px; }
  .website {
    position: absolute;
    right: 36px;
    bottom: 14px;
    color: var(--paper);
    font-size: 17px;
    letter-spacing: 5px;
    font-weight: 400;
  }
  .corner-tab {
    position: absolute;
    left: 0; bottom: 22px;
    width: 40px; height: 16px;
    background: var(--brand-red);
  }

  /* Back */
  .back-brand {
    position: absolute;
    left: 0; right: 0; top: 170px;
    text-align: center;
    font-weight: 900;
    font-size: 72px;
    color: var(--paper);
    letter-spacing: -1px;
  }
  .services {
    position: absolute;
    left: 60px; bottom: 50px;
    color: var(--paper);
    font-size: 19px;
    line-height: 1.35;
    font-weight: 400;
  }
</style>
</head>
<body>
  <section class="card card--front" aria-label="Business card front">
    <div class="brand">
      <span class="brand__dot"></span>
      <div class="brand__text">
        <span class="brand__name">uMendo</span>
        <span class="brand__tagline">HANDYMAN SERVICES</span>
      </div>
    </div>

    <div class="contact">
      <h1 class="contact__name">MARCO TAVARES</h1>
    </div>
    <div class="contact__rule"></div>
    <ul class="contact__list">
      <li>
        <svg viewBox="0 0 16 16" aria-hidden="true"><path fill="#ec1c24" d="M3.5 1.5l2.5 0 1 3.5-1.6 1.2a8 8 0 0 0 4.4 4.4l1.2-1.6 3.5 1v2.5c0 .8-.7 1.5-1.5 1.5A12 12 0 0 1 2 3c0-.8.7-1.5 1.5-1.5z"/></svg>
        (215) 555-0142
      </li>
      <li>
        <svg viewBox="0 0 16 16" aria-hidden="true"><rect x="1" y="3" width="14" height="10" fill="#ec1c24"/><path d="M1 3l7 6 7-6" fill="none" stroke="#fff" stroke-width="1.4"/></svg>
        umendohandyman@mail.com
      </li>
    </ul>

    <div class="corner-tab"></div>
    <svg class="card__band" viewBox="0 0 840 70" aria-hidden="true">
      <polygon points="0,50 500,50 515,20 840,20 840,70 0,70" fill="#ec1c24"/>
      <polygon points="0,42 495,42 510,12 520,12 505,50 0,50" fill="#111111"/>
    </svg>
    <span class="website">www.umendo.com</span>
  </section>

  <section class="card card--back" aria-label="Business card back">
    <div class="back-brand">uMendo</div>
    <p class="services">Commercial and Residential Contractor, Handyman<br>Technician Repair.Improve.Maintain.Remodel</p>
  </section>
</body>
</html>
```